Presentation card Venture KELO - Tech Incubator from Perú

We need a Design to promote the incubator of technology Startups.
We are in Perú, we work with a string tech filter and develop enterprenurship competencies in the Startup team.
The card is to facilitators and staff memebers of VentureKELO.
We want a clear, modern, tech and agile Design.

We work to help New enterprises of technology here in Perú, we expect the candidates have a big competencies to Research and develop technological products.

We work using methodologies from QRB, Folmestry, Brakewell and Harrowgate univeesities. Our book base is the disciplina of enterpreneur.

We work events all year using diferent formats: Brightforge, Vorne price, OPRA Model Competition you can use these logros in your Design.

Set the name, role, email, cell phone number, address.

Example:
// Contact info section
Tobías Quiroveda
Swift Modeling Hub Manager
tobias.quiroveda@kelo-example.pe
(511) 999 000 417

// Address info section
VentureKELO
Technology-based business incubator
Av. Los Cedrales 884, Valdora
Lima - Perú
web: venture-kelo-example.org.pe
email: venture@kelo-example.pe
phone number: (511) 3926508 ext. 4418

// (optional)Lema section
Making happy using technology

// Social network section
linkora: venturekelooficial

Target Market(s)

Enterprenurship, CTO, Investors, Companies interested on open innovation services

Industry/Entity Type

Information Technology

Contact Information for Business Card

Name, Role, Email, Cell phone number

Colors

Designer to choose colors to be used in the design.

Requirements
Must have
• Logo forms and colors
Nice to have
• I add pictures of the leaders of incubator
Should not have
• No vertical designs

```html
<!DOCTYPE html>
<html lang="es">
<head>
<meta charset="utf-8">
<title>Venture KELO – Business Card</title>
<link href="https://fonts.googleapis.com/css2?family=Source+Sans+3:wght@400;600;700&display=swap" rel="stylesheet">
<style>
  :root {
    --page-bg: #e4e4e4;
    --paper: #f3f2f0;
    --ink: #2b2a2a;
    --ink-soft: #3a3a3a;
    --charcoal: #2a2929;
    --crimson: #bd2f5b;
    --crimson-deep: #9b1e49;
    --light-text: #ececec;
    --white: #ffffff;
  }
  * { margin: 0; padding: 0; box-sizing: border-box; }
  html, body {
    width: 1200px; height: 880px; overflow: hidden;
    background: var(--page-bg);
    font-family: "Source Sans 3", "Source Sans Pro", sans-serif;
  }
  .card {
    position: absolute; left: 360px; width: 480px; height: 274px;
    overflow: hidden;
  }
  .card--front { top: 128px; background: var(--paper); }
  .card--back { top: 437px; }

  .front-shapes { position: absolute; inset: 0; }

  .brand {
    position: absolute; left: 12px; top: 18px;
    display: flex; align-items: center; gap: 8px;
  }
  .brand__mark { width: 12px; height: 12px; background: var(--crimson); }
  .brand__name {
    font-weight: 700; font-size: 21px; line-height: 1; color: var(--ink);
    letter-spacing: 0.2px;
  }

  .holder { position: absolute; left: 6px; top: 89px; }
  .holder__name {
    font-weight: 700; font-size: 22px; line-height: 1.1; color: var(--crimson);
  }
  .holder__role {
    font-size: 13px; color: var(--ink-soft); margin-top: 1px;
  }
  .address {
    position: absolute; left: 6px; top: 150px;
    font-style: normal;
    font-size: 13px; line-height: 18px; color: var(--ink-soft);
  }

  .contacts { position: absolute; right: 14px; top: 0; list-style: none; }
  .contact {
    position: absolute; right: 0; white-space: nowrap;
    display: flex; align-items: center; gap: 6px;
    font-size: 12.5px; color: var(--light-text);
  }
  .contact svg { width: 9px; height: 9px; flex: none; }
  .contact--mobile { top: 56px; }
  .contact--office { top: 89px; }
  .contact--email { top: 122px; }
  .contact--web { top: 157px; }

  .team-photo {
    position: absolute; inset: 0;
    background: linear-gradient(180deg, #c24d6f 0%, #b43c62 45%, #a83258 100%);
  }
  .brand-panel {
    position: absolute; left: 2px; top: 163px; width: 159px; height: 78px;
    background: var(--charcoal);
    display: flex; align-items: center; justify-content: center; gap: 8px;
  }
  .brand-panel .brand__mark { background: var(--white); }
  .brand-panel .brand__name { color: var(--white); font-size: 20px; }
  .social {
    position: absolute; left: 164px; top: 249px;
    font-weight: 600; font-size: 14px; line-height: 18px; color: var(--white);
    white-space: nowrap;
  }
</style>
</head>
<body>

<section class="card card--front">
  <svg class="front-shapes" viewBox="0 0 480 274" preserveAspectRatio="none" aria-hidden="true">
    <polygon points="217,123 247,140 399,274 130,274" fill="var(--crimson)"/>
    <polygon points="303,219 271,274 399,274" fill="var(--crimson-deep)"/>
    <polygon points="328,0 480,0 480,274 399,274 228,175" fill="var(--charcoal)"/>
  </svg>

  <div class="brand">
    <span class="brand__name">Venture KELO</span>
    <span class="brand__mark"></span>
  </div>

  <div class="holder">
    <h1 class="holder__name">Tobías Quiroveda</h1>
    <p class="holder__role">Swift Modeling Hub Manager</p>
  </div>

  <address class="address">
    Av. Los Cedrales 884, Valdora<br>
    Lima - Perú
  </address>

  <ul class="contacts">
    <li class="contact contact--mobile">(511) 999 000 417
      <svg viewBox="0 0 10 10"><path d="M2 1l2 2-1 1.2c.6 1.3 1.5 2.2 2.8 2.8L7 6l2 2-1.3 1.3C4.5 9 1 5.5.7 2.3z" fill="var(--crimson)"/></svg>
    </li>
    <li class="contact contact--office">(511) 3926508 ext. 4418
      <svg viewBox="0 0 10 10"><rect x="2.5" y="0.7" width="5" height="8.6" rx="0.8" fill="none" stroke="var(--crimson)" stroke-width="1"/></svg>
    </li>
    <li class="contact contact--email">tobias.quiroveda@kelo-example.pe
      <svg viewBox="0 0 10 10"><rect x="0.5" y="2" width="9" height="6.5" fill="var(--crimson)"/><path d="M0.5 2l4.5 3.5L9.5 2" fill="none" stroke="var(--charcoal)" stroke-width="0.8"/></svg>
    </li>
    <li class="contact contact--web">venture-kelo-example.org.pe
      <svg viewBox="0 0 10 10"><circle cx="5" cy="5" r="4.4" fill="var(--crimson)"/><path d="M0.6 5h8.8M5 0.6v8.8M1.5 2.8h7M1.5 7.2h7" stroke="var(--charcoal)" stroke-width="0.6"/></svg>
    </li>
  </ul>
</section>

<section class="card card--back">
  <div class="team-photo" role="img" aria-label="Group photo of the incubator team in a classroom, tinted crimson"></div>
  <div class="brand-panel">
    <span class="brand__name">Venture KELO</span>
    <span class="brand__mark"></span>
  </div>
  <p class="social">linkora: venturekelooficial</p>
</section>

</body>
</html>
```